Live a healthy life. Kvel

Advertising campaign for reversing type 2 diabetes and insulin resistance. The best way to reverse type 2 diabetes or put it in remission is to prevent it from triggering. We do this by healthy food choices, no overeating and exercise. The final design should promote the aforementioned and should be able to be implemented in society, schools, churches etc. Kvel is the creator of the campaign. Youtube channel "straight from the desk of Kvel"

```html
<!DOCTYPE html>
<html lang="en">
<head>
<meta charset="utf-8">
<title>Live a healthy life – Kvel</title>
<link href="https://fonts.googleapis.com/css2?family=Fira+Sans:wght@400;500;600;700&family=Ubuntu:wght@400;500;700&display=swap" rel="stylesheet">
<style>
:root{
  --teal:#0e7c80;
  --orange:#ee7f1f;
  --red:#cf3a2a;
  --ink:#234e56;
  --paper:#f3f3f3;
  --sky:#6fc4e4;
  --sun:#f6c65c;
  --white:#ffffff;
}
*{margin:0;padding:0;box-sizing:border-box}
html,body{width:800px;height:1200px;overflow:hidden;background:var(--paper)}
.poster{position:relative;width:800px;height:1200px;overflow:hidden;background:var(--paper);font-family:"Ubuntu",sans-serif;color:var(--ink)}
.masthead{position:absolute;left:0;top:0;width:800px;height:126px;background:var(--teal)}
.masthead h1{position:absolute;left:0;right:0;top:36px;text-align:center;font-family:"Fira Sans",sans-serif;font-weight:700;font-size:54px;color:var(--white);line-height:1}
.tagline-rail{position:absolute;left:30px;right:30px;top:116px;height:40px;background:#b9b9b9;border-radius:20px}
.tagline{position:absolute;left:39px;width:722px;top:111px;height:50px;background:var(--orange);border-radius:25px;z-index:3;text-align:center;font-family:"Fira Sans",sans-serif;font-weight:500;font-size:32px;line-height:50px;color:var(--white)}
.hero{position:absolute;left:0;top:148px;width:800px;height:424px;background:linear-gradient(180deg,#cfe6f2 0%,#8fbf6d 35%,#5d8f45 60%,#a9c58a 100%)}
.prevention{position:absolute;left:0;top:436px;width:800px;height:136px;background:rgba(240,236,224,.86)}
.prevention h2{position:absolute;left:69px;top:12px;font-family:"Fira Sans",sans-serif;font-weight:700;font-size:36px;line-height:43px;color:var(--red)}
.prevention p{position:absolute;left:358px;top:13px;font-size:18.5px;line-height:25px;color:var(--ink)}
.prevention strong{color:var(--red);font-weight:700}
.steps-title{position:absolute;left:30px;top:538px;width:740px;height:92px;background:var(--teal);border-radius:46px;text-align:center;font-family:"Fira Sans",sans-serif;font-weight:600;font-size:44px;line-height:92px;color:var(--white)}
.plate{position:absolute;left:-80px;top:648px;width:274px;height:274px;border-radius:50%;background:radial-gradient(circle at 50% 50%,#f5c95a 0%,#e8d45c 55%,#c9e063 70%,#d4e86d 100%)}
.outdoors{position:absolute;left:0;top:0;width:800px;height:1200px}
.controller{position:absolute;left:44px;top:944px;width:274px;height:226px;border-radius:60px 60px 90px 90px;background:linear-gradient(160deg,#4f9a3a,#2f6f25)}
.step{position:absolute}
.step h3{font-family:"Fira Sans",sans-serif;font-weight:600;font-size:41px;line-height:44px;color:var(--orange)}
.step p{font-size:18.5px;line-height:25px;color:var(--ink);margin-top:6px}
.step-eat{left:224px;top:652px}
.step-portion{left:285px;top:808px}
.step-move{left:347px;top:962px}
.channel-mark{position:absolute;left:359px;top:1118px;width:84px;text-align:center;font-family:"Fira Sans",sans-serif;font-weight:700;font-size:30px;color:var(--orange)}
.channel{position:absolute;left:467px;top:1096px;width:360px;height:74px;background:var(--sun);border-radius:37px 0 0 37px}
.channel-icon{position:absolute;left:30px;top:24px;width:28px;height:28px;border-radius:50%;background:var(--red)}
.channel-name{position:absolute;left:68px;top:0;line-height:74px;font-size:17px;font-weight:500;color:var(--ink);white-space:nowrap}
.subscribe{position:absolute;left:559px;top:1081px;width:148px;height:30px;background:var(--red);border-radius:15px;text-align:center;font-family:"Fira Sans",sans-serif;font-weight:700;font-size:19px;line-height:30px;color:var(--white);z-index:2}
</style>
</head>
<body>
<main class="poster">
  <header class="masthead"><h1>“Live a healthy life” Kvel</h1></header>
  <div class="tagline-rail"></div>
  <div class="tagline">Reverse Type 2 Diabetes / Insulin Resistance</div>

  <div class="hero" role="img" aria-label="Photo of four smiling people of different ages jogging together along a tree-lined park path"></div>
  <section class="prevention">
    <h2>START WITH<br>PREVENTION.</h2>
    <p>The best way to reverse or stop type 2<br>diabetes is to <strong>prevent it from starting.</strong><br>Let’s make healthy living a lifestyle!</p>
  </section>

  <div class="steps-title">3 Simple Steps to Fight Diabetes</div>

  <svg class="outdoors" viewBox="0 0 800 1200" aria-hidden="true">
    <path d="M0 911 C110 905 190 940 250 1010 C300 1070 340 1140 370 1200 L0 1200 Z" fill="var(--sky)"/>
  </svg>
  <div class="plate" role="img" aria-label="Plate of grilled salmon with lemon slices and fresh herbs"></div>
  <div class="controller" role="img" aria-label="Grass-covered game controller with flowers and a no sign, lettered GO OUTSIDE"></div>

  <section class="step step-eat">
    <h3>Eat Smart</h3>
    <p>Choose real healthy food:<br>Fruits, veggies, lean proteins and whole grains.<br>Avoid sugary snacks, soda and fried foods</p>
  </section>
  <section class="step step-portion">
    <h3>Don’t Overeat</h3>
    <p>Stop when you are full.<br>Choose portion control over plate overload.<br>Frequency don’t eat and snack all day.</p>
  </section>
  <section class="step step-move">
    <h3>Move Daily</h3>
    <p>Walking, running, riding a bike, dancing, etc.<br>30 minutes a day keeps diabetes away!</p>
  </section>

  <div class="channel-mark">Kvel</div>
  <div class="subscribe">Subscribe</div>
  <div class="channel">
    <span class="channel-icon"></span>
    <span class="channel-name">straight from the desk of Kvel</span>
  </div>
</main>
</body>
</html>
```